Business Card for: Northbrook Financial Advisory Services Inc.

provide strategic financial advisory services to companies in the areas of corporate finance, mergers and acquisitions, executive coaching and strategic planning

Target Market(s)

Companies, banks, accountants, lawyers

Industry/Entity Type

High end business consulting in corporate finance, mergers and acquisitions, consulting

Contact Information for Business Card

Name of company, Name: xxxxxx xxxxxx , CEO, - phone number: 1-xxx-xxx-xxxx, - email address,

Requirements
Must have
• Must be professional and simple.
Nice to have
• simple, straight graphics, must give the impression that we are trustworthy, professional, competent
Should not have
• loud colors, loud design features

```html
<!DOCTYPE html>
<html lang="en">
<head>
<meta charset="utf-8">
<title>Northbrook Financial Advisory Services Inc. — Business Card</title>
<link rel="stylesheet" href="https://fonts.googleapis.com/css2?family=Roboto:ital,wght@0,400;0,500;1,700&display=swap">
<style>
  :root {
    --backdrop: #767676;
    --card: #ffffff;
    --ink: #0d0d0d;
    --blue-light: #29a9e1;
    --blue-mid: #2367b0;
    --blue-deep: #26358c;
    --on-blue: #ffffff;
  }
  html, body {
    margin: 0;
    padding: 0;
    width: 1199px;
    height: 1200px;
    overflow: hidden;
    background: var(--backdrop);
    font-family: "Roboto", Arial, sans-serif;
  }
  .sheet { position: relative; width: 1199px; height: 1200px; }
  .card {
    position: absolute;
    left: 152px;
    width: 895px;
    height: 524px;
    background: var(--card);
    overflow: hidden;
  }
  .card--front { top: 59px; }
  .card--back { top: 620px; }
  .card__art {
    position: absolute;
    inset: 0;
    width: 100%;
    height: 100%;
  }
  .company-name {
    margin: 0;
    font-weight: 700;
    font-style: italic;
    font-size: 35px;
    letter-spacing: -0.2px;
    white-space: nowrap;
  }
  .card--front .company-name {
    position: absolute;
    left: 70px;
    top: 78px;
    color: var(--ink);
  }
  .holder {
    position: absolute;
    left: 70px;
    top: 259px;
    color: var(--on-blue);
  }
  .holder__name {
    margin: 0;
    font-size: 36px;
    font-weight: 500;
    line-height: 1.1;
  }
  .holder__role {
    margin: 8px 0 0;
    font-size: 20px;
    font-weight: 400;
  }
  .contact {
    position: absolute;
    margin: 0;
    padding: 0;
    list-style: none;
    color: var(--on-blue);
    font-size: 22px;
    line-height: 35px;
  }
  .contact--direct { left: 70px; top: 377px; }
  .contact--address { left: 532px; top: 377px; }
  .contact__item { display: flex; align-items: flex-start; }
  .contact__icon {
    width: 16px;
    height: 16px;
    margin: 9px 14px 0 0;
    flex: none;
    fill: var(--on-blue);
  }
  .contact__lines { display: block; white-space: nowrap; }
  .brand-band {
    position: absolute;
    left: 0;
    top: 149px;
    width: 100%;
    height: 228px;
    background: linear-gradient(90deg, var(--blue-light), var(--blue-mid) 55%, var(--blue-deep));
    display: flex;
    align-items: center;
    justify-content: center;
  }
  .card--back .company-name { color: var(--on-blue); }
</style>
</head>
<body>
<main class="sheet">
  <section class="card card--front" aria-label="Card front">
    <svg class="card__art" viewBox="0 0 716 420" preserveAspectRatio="none" aria-hidden="true">
      <defs>
        <linearGradient id="band-gradient" x1="0" y1="0" x2="1" y2="0">
          <stop offset="0" stop-color="var(--blue-light)"/>
          <stop offset="0.55" stop-color="var(--blue-mid)"/>
          <stop offset="1" stop-color="var(--blue-deep)"/>
        </linearGradient>
      </defs>
      <polygon class="accent-step" fill="var(--ink)" points="289,189 444,189 486,238 716,238 716,243 333,243"/>
      <polygon class="info-band" fill="url(#band-gradient)" points="0,164 267,164 333,242 515,242 546,268 577,242 716,242 716,420 0,420"/>
    </svg>

    <h1 class="company-name">Northbrook Financial Advisory Services Inc.</h1>

    <div class="holder">
      <p class="holder__name">Dana Whitfield</p>
      <p class="holder__role">CEO</p>
    </div>

    <ul class="contact contact--direct">
      <li class="contact__item">
        <svg class="contact__icon" viewBox="0 0 24 24" aria-hidden="true"><path d="M6.6 10.8c1.4 2.8 3.8 5.1 6.6 6.6l2.2-2.2c.3-.3.7-.4 1-.2 1.1.4 2.3.6 3.6.6.6 0 1 .4 1 1V20c0 .6-.4 1-1 1C10.6 21 3 13.4 3 4c0-.6.4-1 1-1h3.5c.6 0 1 .4 1 1 0 1.3.2 2.5.6 3.6.1.3 0 .7-.2 1z"/></svg>
        <span>555-0142-7788</span>
      </li>
      <li class="contact__item">
        <svg class="contact__icon" viewBox="0 0 24 24" aria-hidden="true"><path d="M20 4H4c-1.1 0-2 .9-2 2v12c0 1.1.9 2 2 2h16c1.1 0 2-.9 2-2V6c0-1.1-.9-2-2-2zm0 4-8 5-8-5V6l8 5 8-5z"/></svg>
        <span>hello@northbrookfa.com</span>
      </li>
    </ul>

    <ul class="contact contact--address">
      <li class="contact__item">
        <svg class="contact__icon" viewBox="0 0 24 24" aria-hidden="true"><path d="M12 2C8.1 2 5 5.1 5 9c0 5.3 7 13 7 13s7-7.7 7-13c0-3.9-3.1-7-7-7zm0 9.5a2.5 2.5 0 1 1 0-5 2.5 2.5 0 0 1 0 5z"/></svg>
        <span class="contact__lines">418 Larkspur Avenue, Suite 12,<br>Fairmont Bay 40217</span>
      </li>
    </ul>
  </section>

  <section class="card card--back" aria-label="Card back">
    <div class="brand-band">
      <h2 class="company-name">Northbrook Financial Advisory Services Inc.</h2>
    </div>
  </section>
</main>
</body>
</html>
```